Flyer-Design für Handelsunternehmen
Zielgruppe
Wir sind ein Handelsunternehmen für Produkte zur Ladungssicherung im Container.
Unsere Zielgruppe sind Speditionen, Stauer, Logistiker, Exporteure, Industrie & Handel.
Kernprodukte sind Stausäcke, Lashband, Container-Lashing, Container-Planen, Umreifungsband, Plomben sowie Halterungen von FRACHTOMIR®.
Gewünscht sind Flyer (& Broschüren) sowohl zu den einzelnen Produktgruppen wie auch als Gesamtübersicht
(Bilder und Textbeispiele auf www.KTlager57.de bzw. nach Rücksprache)
Der Flyer soll schwerpunktmäßig einen kurzen Überblick über die genannten Produktkategorien abbilden. Damit der Kunde (ausschließlich B2B) weiß, was wir anbieten.
Verkauf findet nicht nur über den Shop statt, sondern auch klassisch per Telefon, Fax und Vertriebsmitarbeiter.
Aufgabenstellung
Bilder und Textbeispiele auf www.KTlager57.de bzw. nach Rücksprache

```html
<!DOCTYPE html>
<html lang="de">
<head>
<meta charset="utf-8">
<title>Kornhagen &amp; Tessler – Ladungssicherung</title>
<link rel="stylesheet" href="https://fonts.googleapis.com/css2?family=Titillium+Web:wght@300;400;700&display=swap">
<style>
  :root {
    --page-bg: #ece8e1;
    --navy: #1f3f8f;
    --band-blue: #3a62b0;
    --white: #ffffff;
    --orange: #f08a2a;
    --sky-top: #5b8fd6;
    --sky-mid: #b9b7d9;
    --sky-warm: #f1c58f;
    --container-red: #c9553a;
    --container-blue: #34507f;
  }
  * { margin: 0; padding: 0; box-sizing: border-box; }
  html, body {
    width: 1200px;
    height: 873px;
    overflow: hidden;
    background: var(--page-bg);
    font-family: "Titillium Web", "Arial Narrow", sans-serif;
  }
  .canvas {
    width: 1200px;
    height: 873px;
    display: flex;
    align-items: center;
    justify-content: center;
  }
  .cover {
    position: relative;
    width: 580px;
    height: 820px;
    overflow: hidden;
    box-shadow: 0 6px 24px rgba(0,0,0,0.18);
  }
  .cover-photo {
    position: absolute;
    inset: 0;
    background: linear-gradient(180deg,
      var(--sky-top) 0%,
      var(--sky-mid) 25%,
      var(--sky-warm) 48%,
      var(--container-red) 62%,
      var(--container-blue) 74%,
      var(--container-red) 88%,
      #b8482f 100%);
  }
  .brand {
    position: absolute;
    top: 38px;
    right: 34px;
    text-align: right;
    color: var(--navy);
    line-height: 0.95;
    text-transform: uppercase;
  }
  .brand-name {
    font-weight: 700;
    font-size: 44px;
    letter-spacing: 1px;
  }
  .brand-field {
    font-weight: 300;
    font-size: 42px;
    letter-spacing: 1px;
  }
  .claim {
    position: absolute;
    top: 215px;
    left: 150px;
    right: 0;
    padding: 26px 34px 28px 36px;
    background: var(--band-blue);
    color: var(--white);
    font-size: 22px;
    font-weight: 400;
    line-height: 1.35;
    letter-spacing: 1.2px;
    text-transform: uppercase;
  }
  .claim strong { font-weight: 700; }
  .edition {
    position: absolute;
    bottom: 56px;
    left: 0;
    padding: 8px 22px 8px 28px;
    background: var(--navy);
    color: var(--orange);
    font-size: 18px;
    letter-spacing: 1.5px;
  }
</style>
</head>
<body>
  <main class="canvas">
    <article class="cover">
      <div class="cover-photo" role="img" aria-label="Foto: gestapelte rote und blaue Frachtcontainer vor bewölktem Abendhimmel"></div>
      <header class="brand">
        <div class="brand-name">Kornhagen &amp; Tessler</div>
        <div class="brand-field">Ladungssicherung</div>
      </header>
      <p class="claim">
        Innovativer <strong>Produkte</strong> und<br>
        effektiver <strong>Systemlösungen</strong><br>
        für die Ladungssicherung
      </p>
      <div class="edition">2018 / 2019</div>
    </article>
  </main>
</body>
</html>
```